An international wholesale business needs letterhead design

Logo file is attached. Please design a letterhead with the following details:

- Company Name and Logo
- Address
- VAT Registration number
- Phone No
- Website address

```html
<!DOCTYPE html>
<html lang="en">
<head>
<meta charset="utf-8">
<title>Corvella Trading Letterhead</title>
<link href="https://fonts.googleapis.com/css2?family=Quicksand:wght@500;600;700&display=swap" rel="stylesheet">
<style>
  :root {
    --backdrop: #d2d3d5;
    --paper: #ffffff;
    --brand-red: #c3262f;
    --accent-grey: #8a9197;
    --ink: #2f2f33;
    --rule: #c4c4c4;
    --signature-tone: #e4e4e6;
  }
  * { margin: 0; padding: 0; box-sizing: border-box; }
  html, body { width: 1200px; height: 1000px; overflow: hidden; background: var(--backdrop); }
  body { position: relative; font-family: "Quicksand", sans-serif; color: var(--ink); font-weight: 500; }

  .letterhead { position: absolute; left: 302px; top: 79px; width: 595px; height: 842px; background: var(--paper); overflow: hidden; }
  .letterhead > * { position: absolute; }

  .header-band { left: 0; top: 52px; width: 385px; height: 51px; background: var(--brand-red); }
  .brand { left: 69px; top: 61px; height: 34px; display: flex; align-items: center; gap: 7px; color: #fff; }
  .brand-dot { width: 30px; height: 30px; border-radius: 50%; background: #fff; }
  .brand-name { font-size: 17px; font-weight: 700; letter-spacing: 0.5px; }
  .header-divider { left: 394px; top: 52px; width: 13px; height: 51px; background: var(--accent-grey); }

  .contact-list { left: 413px; top: 56px; list-style: none; font-size: 10px; line-height: 14px; }
  .contact-list li { display: flex; align-items: center; gap: 5px; }
  .contact-icon { width: 10px; height: 10px; flex: none; }

  .recipient { left: 71px; top: 158px; }
  .recipient .label { font-size: 14px; line-height: 18px; font-weight: 600; }
  .recipient .name { font-size: 15px; line-height: 14px; font-weight: 700; margin-top: 1px; }
  .recipient .details { margin-top: 10px; font-size: 12px; line-height: 16px; }
  .details b, .letter-date b { font-weight: 700; }

  .letter-date { right: 68px; top: 343px; font-size: 12px; line-height: 16px; }

  .letter-body { left: 71px; top: 365px; width: 458px; font-size: 12.5px; line-height: 16px; }
  .letter-body .salutation { margin-bottom: 8px; }
  .letter-body p + p { margin-top: 16px; }
  .letter-body .salutation + p { margin-top: 0; }

  .sign-off { left: 70px; top: 651px; font-size: 12.5px; line-height: 16px; }
  .signature { left: 70px; top: 677px; width: 121px; height: 29px; background: var(--signature-tone); border-radius: 3px; }
  .signer { left: 71px; top: 715px; font-size: 15px; line-height: 14px; font-weight: 700; }

  .vat { left: 0; width: 595px; top: 833px; }
  .footer-info { left: 71px; top: 754px; width: 454px; text-align: center; font-size: 10px; }
  .footer-info .vat-number { line-height: 16px; }
  .footer-info .rule { height: 1.5px; background: var(--rule); margin: 1px 0 4px; }
  .footer-info .address { display: flex; justify-content: center; align-items: center; gap: 5px; line-height: 14px; }
  .footer-band { left: 0; top: 799px; width: 595px; height: 43px; background: var(--brand-red); }
</style>
</head>
<body>
  <main class="letterhead">
    <div class="header-band"></div>
    <div class="brand">
      <span class="brand-dot"></span>
      <span class="brand-name">CORVELLA TRADING</span>
    </div>
    <div class="header-divider"></div>

    <ul class="contact-list">
      <li>
        <svg class="contact-icon" viewBox="0 0 10 10"><circle cx="5" cy="5" r="5" fill="var(--brand-red)"/><path d="M3.2 2.6l1 .9-.5.8c.4.8 1 1.4 1.8 1.8l.8-.5.9 1-.7.8C4.6 7.1 2.9 5.4 2.5 3.3z" fill="#fff"/></svg>
        +01 555 204 16
      </li>
      <li>
        <svg class="contact-icon" viewBox="0 0 10 10"><circle cx="5" cy="5" r="5" fill="var(--brand-red)"/><rect x="2.6" y="3.3" width="4.8" height="3.4" rx=".4" fill="#fff"/><path d="M2.8 3.5L5 5.2l2.2-1.7" stroke="var(--brand-red)" stroke-width=".6" fill="none"/></svg>
        corvella@email.com
      </li>
      <li>
        <svg class="contact-icon" viewBox="0 0 10 10"><circle cx="5" cy="5" r="5" fill="var(--brand-red)"/><circle cx="5" cy="5" r="2.5" stroke="#fff" stroke-width=".6" fill="none"/><ellipse cx="5" cy="5" rx="1" ry="2.5" stroke="#fff" stroke-width=".5" fill="none"/><path d="M2.5 5h5" stroke="#fff" stroke-width=".5"/></svg>
        corvella.com
      </li>
    </ul>

    <section class="recipient">
      <div class="label">To</div>
      <div class="name">Mrs: Mr. Example<br>Name</div>
      <div class="details">
        <b>P:</b> 987654321<br>
        <b>E:</b> example@email.com<br>
        <b>A:</b> Address, City-123
      </div>
    </section>

    <div class="letter-date"><b>Date:</b> 01/01/2022</div>

    <section class="letter-body">
      <p class="salutation">Dear Example Name</p>
      <p>Lorem ipsum dolor sit amet, consectetuer adipiscing elit, sed diam nonummy nibh euismod tincidunt ut laoreet dolore magna aliquam erat volutpat. Ut wisi enim ad minim veniam, quis nostrud exerci tation ullamcorper suscipit lobortis nisl ut aliquip ex ea commodo consequat. Duis autem vel eum iriure dolor in hendrerit in vulputate velit esse molestie consequat, vel illum dolore eu feu.</p>
      <p>Lorem ipsum dolor sit amet, consectetuer adipiscing elit, sed diam nonummy nibh euismod tincidunt ut laoreet dolore magna aliquam erat volutpat. Ut wisi enim ad minim veniam, quis nostrud exerci tation ullamcorper suscipit lobortis nisl ut aliquip ex ea commodo consequat. Duis autem vel eum iriure dolor in hendrerit in vulputate velit esse molestie consequat.</p>
      <p>Lorem ipsum dolor sit amet, consectetuer adipiscing elit, sed diam nonummy nibh euismod tincidunt ut laoreet dolore magna aliquam erat volutpat.</p>
    </section>

    <div class="sign-off">Yours Sincerely</div>
    <div class="signature" role="img" aria-label="Handwritten signature of the sender"></div>
    <div class="signer">Mrs: Mr. Example<br>Name</div>

    <footer class="footer-info">
      <div class="vat-number">VAT registration number : 246801357</div>
      <div class="rule"></div>
      <div class="address">
        <svg class="contact-icon" viewBox="0 0 10 10"><circle cx="5" cy="5" r="5" fill="var(--brand-red)"/><path d="M5 2.2a2 2 0 0 1 2 2c0 1.5-2 3.6-2 3.6S3 5.7 3 4.2a2 2 0 0 1 2-2z" fill="#fff"/><circle cx="5" cy="4.2" r=".7" fill="var(--brand-red)"/></svg>
        48 Harbor Road, Unit 7, State, IL 60410
      </div>
    </footer>
    <div class="footer-band"></div>
  </main>
</body>
</html>
```